Bright Oak Fitness Facility Business Cards

Business Card Design that incorporates the logo and tagline

Target Market(s)

Fitness, People Who Exercise

Contact Information for Business Card

2817 Mossgrove Bend Road
Tavares, Florida 32190
Phone: 352-555-Jump (5867)
www.brightoakfitness.example
info@brightoakfitness.example

Requirements
Must have
• Logo, Address, Website, email and tagline "More Than A Gym". Colors should be red/black/grey/white

```html
<!DOCTYPE html>
<html lang="en">
<head>
<meta charset="utf-8">
<title>Bright Oak Fitness – Business Card</title>
<link rel="stylesheet" href="https://fonts.googleapis.com/css2?family=Federo&family=Source+Sans+3:wght@400;600&display=swap">
<style>
  :root {
    --brand-red: #d50b2e;
    --panel-black: #131415;
    --paper-white: #ffffff;
    --ink-dark: #1a1a1a;
    --icon-light: #f4f4f4;
    --icon-mid: #b9b9b9;
    --icon-dark: #6d6d6d;
  }
  * { margin: 0; padding: 0; box-sizing: border-box; }
  html, body { width: 1200px; height: 714px; overflow: hidden; background: var(--paper-white); }
  .card {
    position: relative;
    width: 1200px;
    height: 714px;
    background: var(--paper-white);
    overflow: hidden;
    font-family: "Source Sans 3", sans-serif;
  }
  .accent-bar {
    position: absolute;
    left: 0; top: 33px;
    width: 78px; height: 648px;
    background: var(--brand-red);
  }
  .dark-panel {
    position: absolute;
    left: 524px; top: 0;
    width: 676px; height: 714px;
    background: var(--panel-black);
  }
  .brand {
    position: absolute;
    left: 110px; top: 290px;
    width: 340px;
    display: flex;
    align-items: center;
    justify-content: center;
    gap: 14px;
  }
  .brand-dot {
    width: 22px; height: 22px;
    border-radius: 50%;
    background: var(--brand-red);
    flex: none;
  }
  .brand-name {
    font-family: "Source Sans 3", sans-serif;
    font-weight: 600;
    font-size: 44px;
    letter-spacing: 0.5px;
    color: var(--ink-dark);
    white-space: nowrap;
  }
  .tagline {
    position: absolute;
    left: 110px; top: 450px;
    width: 340px;
    text-align: center;
    font-family: "Federo", sans-serif;
    font-size: 37px;
    color: var(--ink-dark);
  }
  .contact-list { list-style: none; }
  .contact-row {
    position: absolute;
    left: 501px;
    width: 666px;
    height: 78px;
    background: var(--brand-red);
    display: flex;
    align-items: center;
  }
  .contact-row--phone { top: 130px; }
  .contact-row--web { top: 244px; }
  .contact-row--mail { top: 357px; }
  .contact-row--address { top: 471px; }
  .contact-icon {
    position: absolute;
    left: 88px; top: 4px;
    width: 70px; height: 72px;
  }
  .contact-text {
    position: absolute;
    left: 174px;
    color: var(--paper-white);
    font-size: 28px;
    line-height: 1.3;
    white-space: nowrap;
  }
  .contact-row--mail .contact-text { left: 188px; }
  .contact-row--address .contact-text { left: 168px; line-height: 1.3; }
</style>
</head>
<body>
<div class="card">
  <div class="accent-bar"></div>
  <div class="dark-panel"></div>

  <div class="brand">
    <span class="brand-dot"></span>
    <span class="brand-name">Bright Oak Fitness</span>
  </div>
  <p class="tagline">More Than A Gym</p>

  <svg width="0" height="0" style="position:absolute">
    <defs>
      <radialGradient id="icon-face" cx="40%" cy="35%" r="70%">
        <stop offset="0" stop-color="#ffffff"/>
        <stop offset="0.6" stop-color="#dcdcdc"/>
        <stop offset="1" stop-color="#8e8e8e"/>
      </radialGradient>
      <linearGradient id="icon-rim" x1="0" y1="0" x2="1" y2="1">
        <stop offset="0" stop-color="#f0f0f0"/>
        <stop offset="1" stop-color="#5e5e5e"/>
      </linearGradient>
    </defs>
  </svg>

  <ul class="contact-list">
    <li class="contact-row contact-row--phone">
      <svg class="contact-icon" viewBox="0 0 70 72" aria-hidden="true">
        <path d="M6 70 L10 48 L24 62 Z" fill="url(#icon-rim)"/>
        <circle cx="37" cy="35" r="33" fill="url(#icon-rim)"/>
        <circle cx="37" cy="35" r="27" fill="url(#icon-face)"/>
        <path d="M28 22 c3-2 5-1 6 2 l2 5 c1 2 0 3-2 4 c1 4 4 8 8 10 c1-2 3-3 4-2 l5 3 c2 1 3 3 1 5 c-3 3-7 4-11 2 c-8-4-14-11-16-19 c-1-4 0-8 3-10z" fill="#222"/>
      </svg>
      <span class="contact-text">352-555-Jump (5867)</span>
    </li>
    <li class="contact-row contact-row--web">
      <svg class="contact-icon" viewBox="0 0 70 72" aria-hidden="true">
        <path d="M6 70 L10 48 L24 62 Z" fill="url(#icon-rim)"/>
        <circle cx="37" cy="35" r="33" fill="url(#icon-rim)"/>
        <circle cx="37" cy="35" r="27" fill="url(#icon-face)"/>
        <g fill="none" stroke="#222" stroke-width="2.6">
          <circle cx="35" cy="34" r="12"/>
          <ellipse cx="35" cy="34" rx="5" ry="12"/>
          <line x1="23" y1="34" x2="47" y2="34"/>
          <line x1="25" y1="28" x2="45" y2="28"/>
          <line x1="25" y1="40" x2="45" y2="40"/>
        </g>
        <path d="M40 38 L52 44 L46 46 L50 52 L47 54 L43 48 L39 52 Z" fill="#222" stroke="#eee" stroke-width="1"/>
      </svg>
      <span class="contact-text">www.brightoakfitness.example</span>
    </li>
    <li class="contact-row contact-row--mail">
      <svg class="contact-icon" viewBox="0 0 70 72" aria-hidden="true">
        <path d="M6 70 L10 48 L24 62 Z" fill="url(#icon-rim)"/>
        <circle cx="37" cy="35" r="33" fill="url(#icon-rim)"/>
        <circle cx="37" cy="35" r="27" fill="url(#icon-face)"/>
        <g fill="none" stroke="#222" stroke-width="2.6" stroke-linejoin="round">
          <rect x="23" y="25" width="28" height="20"/>
          <path d="M23 25 L37 37 L51 25"/>
          <path d="M23 45 L33 34 M51 45 L41 34"/>
        </g>
      </svg>
      <span class="contact-text">info@brightoakfitness.example</span>
    </li>
    <li class="contact-row contact-row--address">
      <svg class="contact-icon" viewBox="0 0 70 72" aria-hidden="true">
        <path d="M6 70 L10 48 L24 62 Z" fill="url(#icon-rim)"/>
        <circle cx="37" cy="35" r="33" fill="url(#icon-rim)"/>
        <circle cx="37" cy="35" r="27" fill="url(#icon-face)"/>
        <path d="M37 54 C31 45 26 39 26 32 a11 11 0 0 1 22 0 c0 7-5 13-11 22z" fill="#222"/>
        <circle cx="37" cy="32" r="4.5" fill="#ddd"/>
      </svg>
      <span class="contact-text">2817 Mossgrove Bend Road Tavares,<br>Florida 32190</span>
    </li>
  </ul>
</div>
</body>
</html>
```